Shiatsu in der Kindlichen Entwicklung
Zielgruppe
Frauen, Familien
Aufgabenstellung
Es sollte ein buntes, gemaltes (Buntstift) aber trotzedem elegantes und ansprechendes Desigen haben.
Ich stelle mir einen Flyer vor, der ein Cover hat und kombinierbare einzelnen Seiten, die man dazu stecken kann. Je nach Interesse meiner Kunden.
Jedes Thema hat eine eigene Seite: Shiatsu in der Schwangerschaft, Baby Shiatsu und Kinder Shiatsu, Shiatsu in der Schule, Shiatsu Kurse usw. die dem Flyer beigefügt werden können.
Ich begleite Famielien und Kinder von klein bis gross.
Es sollten drei Abschnitte sein:
1. Shiatsu in der Schwangerschaft
2. Baby Shiatsu
3. Shiatsu mit Kindern

```html
<!DOCTYPE html>
<html lang="de">
<head>
<meta charset="utf-8">
<title>Shiatsu Flyer – Cover, Innenseite und Einlegeblatt</title>
<link rel="stylesheet" href="https://fonts.googleapis.com/css2?family=Jost:wght@400;500;600&family=Caveat+Brush&display=swap">
<style>
  :root {
    --bg: #ffffff;
    --paper: #ffffff;
    --edge: #e2e2e2;
    --red: #9b1c24;
    --green: #6aa841;
    --green-light: #8cc16a;
    --text: #4a4a4a;
    --skin-1: #f3d2bb;
    --skin-2: #d89c78;
  }
  * { box-sizing: border-box; margin: 0; padding: 0; }
  html, body { width: 1200px; height: 848px; overflow: hidden; background: var(--bg); }
  body { position: relative; font-family: "Jost", sans-serif; color: var(--text); }

  .caption {
    position: absolute; top: 160px; font-size: 17px; color: #222; white-space: nowrap;
  }
  .caption small { font-size: 12px; }

  .panel {
    position: absolute; top: 196px; width: 270px; height: 580px;
    background: var(--paper); border: 1px solid var(--edge);
    box-shadow: 0 1px 4px rgba(0,0,0,.12); overflow: hidden;
  }
  .panel--cover { left: 22px; }
  .panel--inside { left: 314px; }
  .panel--insert-front { left: 606px; }
  .panel--insert-back { left: 898px; background: var(--green); border-color: var(--green); }

  .brand { display: flex; flex-direction: column; align-items: center; gap: 6px; }
  .brand__dot { width: 52px; height: 52px; border-radius: 50%; }
  .brand__name { font-size: 11px; font-weight: 500; letter-spacing: .08em; text-transform: uppercase; }

  /* Cover */
  .cover__brand { position: absolute; top: 200px; left: 0; right: 0; }
  .cover__brand .brand__dot { background: var(--red); }
  .cover__brand .brand__name { color: var(--red); }
  .cover__title {
    position: absolute; top: 262px; left: 0; right: 0; text-align: center;
    font-family: "Caveat Brush", cursive; font-size: 34px; color: var(--red); letter-spacing: .02em;
  }
  .cover__quote {
    position: absolute; top: 312px; left: 0; right: 0; text-align: center;
    font-size: 11.5px; line-height: 14px; letter-spacing: .04em; color: #555;
  }
  .illustration { position: absolute; border-radius: 6px; }
  .cover__bees { left: 14px; top: 440px; width: 160px; height: 140px;
    background: linear-gradient(160deg, rgba(155,28,36,.16), rgba(155,28,36,.04)); }

  /* Inside */
  .inside__body { position: absolute; top: 66px; left: 24px; right: 20px; font-size: 8.6px; line-height: 12.6px; }
  .inside__body h3 { color: var(--red); font-size: 9.2px; font-weight: 600; }
  .inside__body p, .inside__body ul { margin-bottom: 9px; }
  .inside__body ul { list-style: none; }
  .inside__body li { padding-left: 6px; text-indent: -6px; }
  .inside__body li::before { content: "• "; }

  /* Insert front */
  .front__bee { left: 10px; top: 24px; width: 70px; height: 110px;
    background: linear-gradient(160deg, rgba(106,168,65,.18), rgba(106,168,65,.04)); }
  .front__brand { position: absolute; top: 24px; left: 100px; }
  .front__brand .brand__dot { width: 56px; height: 56px; background: var(--green); }
  .front__brand .brand__name { color: var(--green); }
  .front__title {
    position: absolute; top: 96px; left: 0; right: 0; text-align: center;
    font-family: "Caveat Brush", cursive; font-size: 42px; color: var(--green); letter-spacing: .04em;
  }
  .front__subtitle, .front__heading {
    position: absolute; left: 0; right: 0; text-align: center; color: var(--green);
    font-size: 15px; letter-spacing: .06em; text-transform: uppercase;
  }
  .front__subtitle { top: 150px; }
  .front__heading { top: 268px; }
  .front__text {
    position: absolute; left: 18px; right: 18px; font-size: 7.6px; line-height: 10.6px; text-align: justify;
  }
  .front__text--intro { top: 175px; }
  .front__text--areas { top: 292px; }
  .front__bees { right: 14px; top: 340px; width: 110px; height: 100px;
    background: linear-gradient(160deg, rgba(106,168,65,.18), rgba(106,168,65,.04)); }
  .front__photo { position: absolute; left: 0; right: 0; bottom: 0; height: 190px;
    background: radial-gradient(ellipse at 50% 70%, var(--skin-1), var(--skin-2) 70%, #f4f1ee 100%); }
  .front__stroke { position: absolute; left: 0; top: 384px; width: 270px; height: 12px; }

  /* Insert back */
  .back__brand { position: absolute; top: 226px; left: 0; right: 0; }
  .back__brand .brand__dot { width: 66px; height: 66px; background: #fff; }
  .back__brand .brand__name { color: #fff; }
  .back__bees { left: 14px; top: 440px; width: 160px; height: 140px;
    background: linear-gradient(160deg, rgba(255,255,255,.22), rgba(255,255,255,.05)); }
</style>
</head>
<body>

  <div class="caption" style="left:314px;">Flyer Innenseite</div>
  <div class="caption" style="left:606px;">Einlegeblatt Vorderseite</div>
  <div class="caption" style="left:898px;">Einlegeblatt Rückseite <small>Variante 1</small></div>

  <section class="panel panel--cover">
    <div class="brand cover__brand">
      <span class="brand__dot"></span>
      <span class="brand__name">Hanami Shiatsu</span>
    </div>
    <h1 class="cover__title">TCM &amp; SHIATSU</h1>
    <p class="cover__quote">„Jahrtausende alte<br>fernöstliche Medizin,<br>verknüpft mit<br>dem Wissen der<br>modernen Medizin.“</p>
    <div class="illustration cover__bees" role="img" aria-label="Gezeichnete rote Bienen mit gepunkteten Flugbahnen"></div>
  </section>

  <section class="panel panel--inside">
    <div class="inside__body">
      <h3>Methode</h3>
      <p>Die Behandlungsmethode Shiatsu bedeutet „Fingerdruck“. Sie gehört zu den sanften Verfahren der Komplementärmedizin.</p>
      <h3>Anwendungsgebiete</h3>
      <ul>
        <li>Zur Unterstützung der Entwicklung von Babys und Kindern</li>
        <li>In der Schwangerschaft</li>
        <li>Bei Rückenschmerzen, Nackenverspannung und vielem mehr</li>
        <li>Bei chronischen oder wiederkehrenden Beschwerden</li>
        <li>Bei Schlafproblemen</li>
        <li>Bei seelischen Belastungen</li>
        <li>Genesung nach Krankheit</li>
        <li>Allgemeine Förderung der Gesundheit</li>
      </ul>
      <h3>Wie wirkt Shiatsu</h3>
      <p>Die gesunden Kräfte im Menschen werden auf körperlicher, seelischer und geistiger Ebene unterstützt und gestärkt. Durch angemessene Berührung wird Gleichgewicht hergestellt und Blockaden lösen sich.</p>
      <h3>Behandlungsablauf</h3>
      <p>Der Patient liegt in bequemer Kleidung auf einer Matte. Es werden spezielle Techniken wie Daumendruck, Gelenkdehnung und Halten eingesetzt. Die Behandlung ist sanft.</p>
      <p><h3 style="display:inline">Kosten</h3> 1 Stunde/100 CHF</p>
      <p>Die Kosten werden von den meisten Zusatzversicherungen teilweise oder ganz übernommen. Ich empfehle Ihnen, sich bei Ihrer Zusatzversicherungen zu informieren.</p>
    </div>
  </section>

  <section class="panel panel--insert-front">
    <div class="illustration front__bee" role="img" aria-label="Gezeichnete grüne Biene mit gepunkteter Flugbahn"></div>
    <div class="brand front__brand">
      <span class="brand__dot"></span>
    </div>
    <h2 class="front__title">SHIATSU</h2>
    <div class="front__subtitle">In der Schwangerschaft</div>
    <p class="front__text front__text--intro">Wussten Sie, dass Shiatsu eine wunderbare Methode ist während der Schwangerschaft? Es wirkt unterstützend, begleitend, geburtsvorbereitend und sehr entspannend. Diese Ruhe gibt den nötigen Raum, den oftmals kräfteraubenden Alltag auszublenden und wieder in den eigenen Körper zu lauschen. Dabei findet eine natürliche und innige Verbindung mit dem Baby statt. Das ist kraftspendend und harmonisierend.</p>
    <div class="front__heading">Anwendungsgebiete</div>
    <p class="front__text front__text--areas">Morgendlicher Übelkeit, Rückenschmerzen, Wassereinlagerungen, Schlafprobleme, Freude, Sorge, Ängste, Erfahrungen vorangegangener Geburten, Partnerübungen für alle Phasen der Geburt.</p>
    <div class="illustration front__bees" role="img" aria-label="Zwei gezeichnete grüne Bienen mit gepunkteten Flugbahnen"></div>
    <div class="front__photo" role="img" aria-label="Foto: Schwangere Frau hält die Hände um ihren Babybauch"></div>
    <svg class="front__stroke" viewBox="0 0 270 12" preserveAspectRatio="none" aria-hidden="true">
      <path d="M0 4 C70 0 170 3 270 10" stroke="#6aa841" stroke-width="3.5" fill="none" stroke-linecap="round"/>
    </svg>
  </section>

  <section class="panel panel--insert-back">
    <div class="brand back__brand">
      <span class="brand__dot"></span>
      <span class="brand__name">Hanami Shiatsu</span>
    </div>
    <div class="illustration back__bees" role="img" aria-label="Gezeichnete weiße Bienen mit gepunkteten Flugbahnen"></div>
  </section>

</body>
</html>
```